"Rise. Shift. Thrive." Empowerment Book Cover

Hello, I need a hot, trendy, and contemporary book cover designed for my first book called "Rise. Shift. Thrive. -- 360 Bold Momentum Notes to Guide Anyone to Rise, Shift, and Thrive in Their Career & Daily Dreams."
This is my first book and I am really wanting to launch my brand with it... it would be awesome to match the inside/outside branding of the book. So we can either create the book cover to match the book guts, or update the book guts to match the cover.
Lastly, I just got a professional photoshoot done last week so we can use one of those images, or we can go with a different idea/style for the cover. The body of the book is attached. All questions welcomed, happy designing!
Target Market(s)
Gen Z, Millennials and Gen X.
Industry/Entity Type
Personal Development.
Requirements
Must have
- It must stand out and be different from other typical book covers.
Nice to have
- Success, Inspiration, Motivation, Mindset, Growth.
Should not have
- Clipart, stock art, stock look and feel.

```html
<!DOCTYPE html>
<html lang="en">
<head>
<meta charset="utf-8">
<title>Rise. Shift. Thrive. – Cover and Interior Spread</title>
<link rel="stylesheet" href="https://fonts.googleapis.com/css2?family=Bebas+Neue&family=Montserrat:wght@400&family=Arimo:wght@400&display=swap">
<style>
  :root {
    --teal: #00baa7;
    --white: #ffffff;
    --stage: #e8e8e8;
    --band-grey: #bfbfbf;
    --ink: #111111;
  }
  html, body {
    margin: 0;
    padding: 0;
    width: 1200px;
    height: 889px;
    overflow: hidden;
    background: var(--stage);
  }
  .spread { display: block; width: 1200px; height: 889px; }
  .cover-bg { fill: var(--teal); }
  .title-box { fill: var(--white); }
  .author {
    font-family: "Montserrat", sans-serif;
    font-weight: 400;
    font-size: 33px;
    letter-spacing: 0.36em;
    fill: var(--white);
  }
  .title-word {
    font-family: "Bebas Neue", sans-serif;
    fill: var(--teal);
  }
  .subtitle {
    font-family: "Bebas Neue", sans-serif;
    font-size: 37px;
    fill: var(--white);
  }
  .page { fill: var(--white); }
  .band-teal { fill: var(--teal); }
  .band-grey { fill: var(--band-grey); }
  .section-label {
    font-family: "Bebas Neue", sans-serif;
    font-size: 31px;
    fill: var(--white);
  }
  .tip {
    font-family: "Arimo", Arial, sans-serif;
    font-size: 19px;
    fill: var(--ink);
  }
</style>
</head>
<body>
<svg class="spread" viewBox="0 0 1200 889" xmlns="http://www.w3.org/2000/svg">
  <!-- Front cover -->
  <g class="cover">
    <rect class="cover-bg" x="37" y="33" width="552" height="823"/>
    <text class="author" x="316" y="92" text-anchor="middle">DANIEL OKAFOR</text>

    <rect class="title-box" x="37" y="135" width="233" height="179"/>
    <text class="title-word" x="51" y="302" font-size="214" textLength="202" lengthAdjust="spacingAndGlyphs">RISE</text>

    <rect class="title-box" x="37" y="331" width="457" height="179"/>
    <text class="title-word" x="51" y="498" font-size="214" textLength="427" lengthAdjust="spacingAndGlyphs">SHIFT</text>

    <rect class="title-box" x="37" y="531" width="552" height="179"/>
    <text class="title-word" x="51" y="705" font-size="236" textLength="495" lengthAdjust="spacingAndGlyphs">THRIVE</text>

    <text class="subtitle" x="100" y="791" textLength="426" lengthAdjust="spacingAndGlyphs">360 BOLD MOMENTUM NOTES TO GUIDE ANYONE TO</text>
    <text class="subtitle" x="60" y="833" textLength="506" lengthAdjust="spacingAndGlyphs">RISE, SHIFT AND THRIVE IN THEIR CAREER AND DAILY DREAMS</text>
  </g>

  <!-- Interior page: opening section -->
  <g class="interior-page">
    <rect class="page" x="614" y="33" width="552" height="382"/>
    <rect class="band-grey" x="689" y="55" width="477" height="44"/>
    <rect class="band-teal" x="614" y="55" width="75" height="44"/>
    <text class="section-label" x="638" y="88">RISE</text>

    <text class="tip" text-anchor="middle">
      <tspan x="890" y="160">TIP 1.</tspan>
      <tspan x="890" y="180">Forget trying to be</tspan>
      <tspan x="890" y="200">the next anyone.</tspan>
      <tspan x="890" y="220">Just be the first you.</tspan>
    </text>
    <text class="tip" text-anchor="middle">
      <tspan x="890" y="304">TIP 2.</tspan>
      <tspan x="890" y="324">Your chances of success in life</tspan>
      <tspan x="890" y="344">greatly increase when you</tspan>
      <tspan x="890" y="364">focus on unlearning before learning.</tspan>
    </text>
  </g>

  <!-- Interior page: closing section -->
  <g class="interior-page">
    <rect class="page" x="614" y="473" width="552" height="383"/>
    <rect class="band-teal" x="614" y="495" width="552" height="44"/>
    <text class="section-label" x="638" y="528">THRIVE</text>

    <text class="tip" text-anchor="middle">
      <tspan x="890" y="604">TIP 359.</tspan>
      <tspan x="890" y="624">Reject fear</tspan>
      <tspan x="890" y="644">Embrace love.</tspan>
    </text>
    <text class="tip" text-anchor="middle">
      <tspan x="892" y="749">TIP 360.</tspan>
      <tspan x="892" y="769">You can only finish</tspan>
      <tspan x="892" y="789">that which you start.</tspan>
    </text>
  </g>
</svg>
</body>
</html>
```